Land Buying Company Needs Letterhead for Direct Mail Marketing to Land Owners

We are looking for a professional letterhead that we will be including in our direct mail marketing. We will be sending this to land owners who may be interested in selling or purchasing land.

The letterhead needs to be editable. Headers and footers would look nice, but we are open. We would want it to include our address, website, phone, and email info. For right now the address to use for design purposes would the following:

Address: 415 Bramwell Avenue #600
Dallas, TX 75219
Website - www.quillridgeacres.example
Email - info@quillridgeacres.example
Phone - 866-402-ACRE

I have attached our logo zip file that we just had done on Pixel Guild. Let me know what questions you have, and thank you.

```html
<!DOCTYPE html>
<html lang="en">
<head>
<meta charset="utf-8">
<title>Quillridge Acres Letterhead</title>
<link href="https://fonts.googleapis.com/css2?family=Montserrat:wght@400;500;700&display=swap" rel="stylesheet">
<style>
  :root {
    --backdrop: #787878;
    --paper: #ffffff;
    --forest: #4f6a32;
    --forest-deep: #435a29;
    --lime: #9dc32a;
    --ink: #2f2f2f;
    --white: #ffffff;
  }
  * { margin: 0; padding: 0; box-sizing: border-box; }
  html, body { width: 969px; height: 1200px; overflow: hidden; background: var(--backdrop); }
  body { position: relative; font-family: "Montserrat", Arial, sans-serif; }

  .letterhead { position: absolute; left: 91px; top: 78px; width: 784px; height: 1014px; background: var(--paper); overflow: hidden; }

  .header { position: absolute; left: 0; top: 0; width: 784px; height: 137px; background: var(--forest); }
  .header-forest { position: absolute; inset: 0; background: linear-gradient(180deg, #54703a 0%, #4a6430 60%, #435a29 100%); }

  .brand { position: absolute; left: 61px; top: 52px; display: flex; align-items: center; gap: 14px; }
  .brand-dot { width: 64px; height: 64px; border-radius: 50%; background: var(--white); }
  .brand-name { font-weight: 700; font-size: 26px; letter-spacing: 1.5px; color: var(--lime); text-transform: uppercase; }

  .contact { position: absolute; left: 539px; top: 57px; list-style: none; color: var(--white); font-size: 12.3px; line-height: 1; }
  .contact li { position: relative; padding-left: 18px; margin-bottom: 5px; }
  .contact li.address { line-height: 16px; margin-top: 8px; }
  .contact svg { position: absolute; left: 0; top: 1px; width: 11px; height: 11px; }

  .rule { position: absolute; left: 0; top: 145px; width: 520px; height: 5px; background: var(--lime); }
  .web-tab { position: absolute; left: 512px; top: 145px; width: 272px; height: 23px; background: var(--lime);
             clip-path: polygon(0 0, 100% 0, 100% 100%, 14px 100%); }
  .web-tab span { position: absolute; left: 29px; top: 5px; font-size: 12px; font-weight: 700; color: var(--forest-deep); }

  .content { position: absolute; left: 72px; top: 259px; width: 648px; }
  .content h1 { font-size: 16px; font-weight: 700; color: var(--lime); }
  .content .underline { width: 56px; height: 3px; background: var(--forest); margin: 4px 0 15px 1px; }
  .content p { font-size: 13px; line-height: 20.4px; color: var(--ink); margin-bottom: 25px; }

  .signature { position: absolute; left: 518px; top: 846px; width: 190px; border-top: 1px solid var(--forest); text-align: center; }
  .signature span { display: block; margin-top: 14px; font-size: 20px; font-weight: 700; color: var(--forest); }

  .footer-forest { position: absolute; left: 0; top: 913px; width: 784px; height: 101px;
                   background: linear-gradient(180deg, rgba(79,106,50,0.15) 0%, #4f6a32 60%, #435a29 100%); }
</style>
</head>
<body>
  <main class="letterhead">
    <header class="header">
      <div class="header-forest" role="img" aria-label="Pine forest silhouette across the header"></div>
      <div class="brand">
        <div class="brand-dot"></div>
        <div class="brand-name">Quillridge Acres</div>
      </div>
      <ul class="contact">
        <li>
          <svg viewBox="0 0 12 12"><circle cx="6" cy="6" r="6" fill="#9dc32a"/><path d="M4 3l1.2 1.5-.6.8c.4.8 1 1.4 1.8 1.8l.8-.6L8.7 8 8 9C5.5 8.7 3.3 6.5 3 4z" fill="#4f6a32"/></svg>
          866-402-ACRE
        </li>
        <li>
          <svg viewBox="0 0 12 12"><circle cx="6" cy="6" r="6" fill="#9dc32a"/><rect x="3" y="4" width="6" height="4.2" fill="#fff"/><path d="M3 4l3 2.3L9 4" stroke="#9dc32a" stroke-width=".8" fill="none"/></svg>
          info@quillridgeacres.example
        </li>
        <li class="address">
          <svg viewBox="0 0 12 12"><path d="M6 0a4.3 4.3 0 0 0-4.3 4.3C1.7 7.5 6 12 6 12s4.3-4.5 4.3-7.7A4.3 4.3 0 0 0 6 0z" fill="#9dc32a"/><circle cx="6" cy="4.3" r="1.6" fill="#4f6a32"/></svg>
          415 Bramwell Avenue #600<br>Dallas, TX 75219
        </li>
      </ul>
    </header>

    <div class="rule"></div>
    <div class="web-tab"><span>www.quillridgeacres.example</span></div>

    <section class="content">
      <h1>Lorem Ipsum?</h1>
      <div class="underline"></div>
      <p>Lorem Ipsum is simply dummy text of the printing and typesetting industry. Lorem Ipsum has been the industry's standard dummy text ever since the 1500s, when an unknown printer took a galley of type and scrambled it to make a type specimen book. It has survived not only five centuries, but also the leap into electronic typesetting, remaining essentially unchanged. It was popularised in the 1960s with the release of Typeforge sheets containing Lorem Ipsum passages, and more recently with desktop publishing software like Quarto LayoutPro including versions of Lorem Ipsum.</p>
      <p>Contrary to popular belief, Lorem Ipsum is not simply random text. It has roots in a piece of classical Latin literature from 45 BC, making it over 2000 years old. Darren Holloway, a Latin professor at Linden Crest College in Virginia, looked up one of the more obscure Latin words, consectetur, from a Lorem Ipsum passage, and going through the cites of the word in classical literature, discovered the undoubtable source. Lorem Ipsum comes from sections 1.10.32 and 1.10.33 of "de Finibus Bonorum et Malorum" (The Extremes of Good and Evil) by Maren Thale, written in 45 BC. This book is a treatise on the theory of ethics, very popular during the Renaissance. The first line of Lorem Ipsum, "Lorem ipsum dolor sit amet..", comes from a line in section 1.10.32.</p>
      <p>The standard chunk of Lorem Ipsum used since the 1500s is reproduced below for those interested. Sections 1.10.32 and 1.10.33 from "de Finibus Bonorum et Malorum" by Maren Thale are also reproduced in their exact original form, accompanied by English versions from the 1914 translation by J. Penwick.</p>
    </section>

    <div class="signature"><span>Signature</span></div>

    <footer class="footer-forest" role="img" aria-label="Pine tree line silhouette along the bottom edge"></footer>
  </main>
</body>
</html>
```